Lumo Brew Premium Matcha brand Label

This is a label design project for a luxury tea brand. Feel free to be creative within the guidelines.
Attached to this project is a document called “Private Label Design Requirements” with the design guidelines and template. There is another document called "Lumo Brew Packaging Instructions" this has more details necessary to stick to the guidelines in the first document.

I have also attached the certifications to be included as well as different variations of the logo for you to use.

If you have any questions, I am here.
Updates

Target Market(s)

Young, active, fun, enjoy the finer things

```html
<!DOCTYPE html>
<html lang="en">
<head>
<meta charset="UTF-8">
<title>Lumo Brew Premium Matcha Label</title>
<link rel="stylesheet" href="https://fonts.googleapis.com/css2?family=Cinzel:wght@400&family=Parisienne&family=Open+Sans:wght@400;600&display=swap">
<style>
  :root {
    --backdrop: #a3b0ac;
    --label-cream: #ece9d4;
    --leaf-green: #8db866;
    --leaf-pale: #c9d9ac;
    --petal-white: #f6f5ec;
    --ink: #3d463a;
    --ink-soft: #5b6456;
    --badge-blue: #3a6a8e;
    --badge-green: #4e8a45;
  }
  * { margin: 0; padding: 0; box-sizing: border-box; }
  html, body { width: 1200px; height: 675px; overflow: hidden; }
  body {
    background: var(--backdrop);
    font-family: "Open Sans", sans-serif;
    color: var(--ink);
    position: relative;
  }
  .label-panel {
    position: absolute;
    top: 296px;
    width: 246px;
    height: 134px;
    background: var(--label-cream);
    overflow: hidden;
  }
  .panel-back { left: 168px; }
  .panel-front { left: 477px; }
  .panel-side { left: 781px; }

  .floral-art {
    position: absolute;
    border-radius: 50%;
  }
  .panel-back .floral-art {
    right: -30px; top: 6px; width: 140px; height: 124px;
    background: radial-gradient(circle at 45% 40%, var(--petal-white) 0%, var(--leaf-pale) 55%, rgba(236,233,212,0) 75%);
  }
  .panel-back .wrap-word {
    position: absolute; right: -14px; top: 72px;
    font-family: "Cinzel", serif; font-size: 30px; color: var(--leaf-green);
  }
  .panel-back .wrap-tag {
    position: absolute; right: 4px; top: 54px;
    font-family: "Parisienne", cursive; font-size: 11px; color: var(--ink-soft);
  }
  .distributor-text {
    position: absolute; left: 16px; top: 71px;
    font-size: 5px; line-height: 9px; color: var(--ink-soft);
  }

  .panel-front .floral-art.left {
    left: -22px; top: 30px; width: 60px; height: 100px;
    background: radial-gradient(ellipse at 60% 50%, var(--leaf-green) 0%, var(--leaf-pale) 55%, rgba(236,233,212,0) 78%);
  }
  .panel-front .floral-art.right {
    right: -22px; top: 30px; width: 60px; height: 100px;
    background: radial-gradient(ellipse at 40% 50%, var(--leaf-green) 0%, var(--leaf-pale) 55%, rgba(236,233,212,0) 78%);
  }
  .brand-mark {
    position: absolute; top: 14px; left: 0; width: 100%;
    display: flex; justify-content: center; align-items: center; gap: 5px;
    font-size: 8px; font-weight: 600; color: var(--ink);
  }
  .brand-mark .dot {
    width: 8px; height: 8px; border-radius: 50%; background: var(--leaf-green);
  }
  .grade-line {
    position: absolute; top: 41px; left: 0; width: 100%;
    display: flex; justify-content: center; align-items: center; gap: 4px;
    font-family: "Parisienne", cursive; font-size: 13px; color: var(--ink);
  }
  .grade-line .rule { width: 14px; height: 1px; background: var(--ink); }
  .product-name {
    position: absolute; top: 56px; left: 0; width: 100%; text-align: center;
    font-family: "Cinzel", serif; font-size: 42px; line-height: 1; color: var(--leaf-green);
    letter-spacing: 1px;
  }
  .net-weight {
    position: absolute; top: 106px; left: 0; width: 100%; text-align: center;
    font-size: 8px; color: var(--ink);
  }

  .panel-side .floral-art {
    left: -40px; top: 4px; width: 130px; height: 124px;
    background: radial-gradient(circle at 55% 40%, var(--petal-white) 0%, var(--leaf-pale) 50%, rgba(236,233,212,0) 74%);
  }
  .ingredients {
    position: absolute; left: 104px; top: 14px; width: 136px;
    font-size: 7px; line-height: 10px; color: var(--ink-soft);
  }
  .ingredients h2 { font-size: 9px; font-weight: 400; margin-bottom: 4px; }
  .ingredients .source { font-weight: 600; color: var(--ink); margin-bottom: 2px; }
  .ingredients ul { list-style: none; }
  .ingredients li::before { content: "• "; }
  .cert-row {
    position: absolute; left: 104px; top: 100px;
    display: flex; align-items: center; gap: 5px;
  }
  .cert-square { width: 24px; height: 18px; background: var(--badge-blue); }
  .cert-circle { width: 18px; height: 18px; border-radius: 50%; background: var(--badge-green); }
  .storage-note { font-size: 6px; line-height: 8px; font-weight: 600; color: var(--ink-soft); }
</style>
</head>
<body>
  <section class="label-panel panel-back">
    <div class="floral-art" role="img" aria-label="White blossom and green leaf illustration"></div>
    <span class="wrap-tag">Premi</span>
    <span class="wrap-word">MA</span>
    <p class="distributor-text">
      Distributed by Lumo Brew Co. | Fernvale, OR<br>
      Certified Organic by Leafline<br>
      PRODUCT OF JAPAN
    </p>
  </section>

  <section class="label-panel panel-front">
    <div class="floral-art left" role="img" aria-label="Green tea leaf illustration"></div>
    <div class="floral-art right" role="img" aria-label="Green tea leaf illustration"></div>
    <div class="brand-mark"><span class="dot"></span>Lumo Brew</div>
    <div class="grade-line"><span class="rule"></span>Premium Organic Ceremonial<span class="rule"></span></div>
    <h1 class="product-name">MATCHA</h1>
    <p class="net-weight">Net Wt: 30g (1.06oz)</p>
  </section>

  <section class="label-panel panel-side">
    <div class="floral-art" role="img" aria-label="White blossom and green leaf illustration"></div>
    <div class="ingredients">
      <h2>Ingredients</h2>
      <p class="source">Premium Organic Japanese Matcha Green Tea</p>
      <ul>
        <li>2 tsp of Matcha</li>
        <li>2oz of Water (170-180 degrees F)</li>
        <li>Whisk in a W formation until frothy</li>
        <li>Sweeten to taste</li>
      </ul>
    </div>
    <div class="cert-row">
      <span class="cert-square"></span>
      <span class="cert-circle"></span>
      <span class="storage-note">KEEP REFRIGERATED<br>FOR QUALITY</span>
    </div>
  </section>
</body>
</html>
```